K7 Dynamics Stationery Design Project

We are looking to have stationary designs created for our company branding materials. We are looking for the following to be created.
1. Business Cards (front & back)
2. Letterhead
3. Envelopes #10
We are a new web design, development and marketing firm. Primary color scheme is desired to be blue/grey/white. This web start-up is owned and operated by individuals with 15+ years experience each in the industry so should not look as though it is a start-up by young/inexperienced individuals.
We build website & custom applications/software. In addition we provide the full spectrum of web marketing solutions including SEO, PPC, Social Media, Branding, Content Marketing and PR.
Please let us know if you have any questions. Looking forward to seeing all the amazing design ideas.
Attached is our logo.
Thanks!
Target Market(s)
Company will be nearly 100% business to business sales. Looking to work with companies that are already established, with a website, who want to take their website and/or online marketing efforts to the next level.
Industry/Entity Type
Marketing
Look and feel

```html
<!DOCTYPE html>
<html lang="en">
<head>
<meta charset="utf-8">
<title>K7 Dynamics – Business Cards</title>
<link href="https://fonts.googleapis.com/css2?family=Jost:wght@400;500;700;800&display=swap" rel="stylesheet">
<style>
  :root {
    --page-bg: #e9eaec;
    --card-white: #ffffff;
    --card-panel: #f3f4f5;
    --card-black: #141516;
    --card-black-glow: #2a2d30;
    --brand-blue: #1a7fc4;
    --ink-dark: #2b2b2b;
    --ink-grey: #555a5f;
    --ink-light: #8a8f94;
    --shadow: rgba(0, 0, 0, 0.14);
  }
  * { box-sizing: border-box; margin: 0; padding: 0; }
  html, body { width: 1200px; height: 1000px; overflow: hidden; }
  body {
    background: var(--page-bg);
    font-family: "Jost", "Futura", sans-serif;
    display: flex;
    align-items: center;
    justify-content: center;
    gap: 40px;
  }
  .card {
    width: 540px;
    height: 310px;
    position: relative;
    overflow: hidden;
    box-shadow: 0 6px 18px var(--shadow);
  }
  /* Front */
  .card-front { background: var(--card-white); }
  .card-front .contact-panel {
    position: absolute;
    inset: 0;
    background: var(--card-panel);
    clip-path: polygon(58% 0, 100% 0, 100% 100%, 45% 100%);
  }
  .brand {
    position: absolute;
    display: flex;
    flex-direction: column;
    align-items: flex-start;
  }
  .card-front .brand { left: 40px; top: 118px; }
  .brand-row { display: flex; align-items: center; gap: 10px; }
  .brand-dot {
    width: 22px; height: 22px;
    border-radius: 50%;
    background: var(--brand-blue);
  }
  .brand-name {
    font-weight: 800;
    font-size: 30px;
    letter-spacing: 0.5px;
    color: var(--ink-dark);
    text-transform: uppercase;
    line-height: 1;
  }
  .brand-tagline {
    margin-top: 6px;
    font-size: 11.5px;
    font-weight: 500;
    color: var(--ink-dark);
  }
  .contact {
    position: absolute;
    left: 300px;
    top: 52px;
    color: var(--ink-grey);
  }
  .person-name {
    font-weight: 700;
    font-size: 17px;
    color: var(--brand-blue);
  }
  .person-title {
    font-size: 12px;
    color: var(--ink-light);
    margin-bottom: 16px;
  }
  .address { font-size: 12.5px; line-height: 1.4; margin-bottom: 10px; }
  .contact-list { list-style: none; font-size: 12.5px; line-height: 1.75; }
  .contact-list li { display: flex; align-items: center; gap: 10px; }
  .contact-list svg { width: 14px; height: 14px; fill: var(--brand-blue); flex: none; }
  /* Back */
  .card-back {
    background: radial-gradient(ellipse at 50% 35%, var(--card-black-glow) 0%, var(--card-black) 65%);
  }
  .card-back .brand {
    left: 50%; top: 50%;
    transform: translate(-50%, -50%);
  }
  .card-back .brand-name { color: var(--card-white); }
  .card-back .brand-tagline { color: var(--card-white); }
</style>
</head>
<body>

  <section class="card card-front" aria-label="Business card front">
    <div class="contact-panel"></div>
    <div class="brand">
      <div class="brand-row">
        <span class="brand-dot"></span>
        <span class="brand-name">K7 Dynamics</span>
      </div>
      <span class="brand-tagline">Web Design, Development and Marketing</span>
    </div>
    <div class="contact">
      <p class="person-name">Daniel R. Marlow</p>
      <p class="person-title">Chairman</p>
      <p class="address">West Harbor Lane, Suite 14<br>P.O. Box 31870 Dunmore<br>Vermont 05720-4193</p>
      <ul class="contact-list">
        <li>
          <svg viewBox="0 0 16 16" aria-hidden="true"><path d="M3 1h3l1.5 4-2 1.2a9 9 0 0 0 4.3 4.3L11 8.5l4 1.5v3a2 2 0 0 1-2 2A12 12 0 0 1 1 3a2 2 0 0 1 2-2z"/></svg>
          (555) 318-2094
        </li>
        <li>
          <svg viewBox="0 0 16 16" aria-hidden="true"><path d="M4.5 0h7A1.5 1.5 0 0 1 13 1.5v13a1.5 1.5 0 0 1-1.5 1.5h-7A1.5 1.5 0 0 1 3 14.5v-13A1.5 1.5 0 0 1 4.5 0zM5 2v10h6V2zm3 11a1 1 0 1 0 0 2 1 1 0 0 0 0-2z"/></svg>
          (555) 476-9013
        </li>
        <li>
          <svg viewBox="0 0 16 16" aria-hidden="true"><path d="M8 0a8 8 0 1 0 4 14.9l-.8-1.6A6.2 6.2 0 1 1 14.2 8v.8c0 .9-.6 1.5-1.3 1.5s-1.2-.6-1.2-1.5V4.5h-1.6v.7A3.8 3.8 0 1 0 10.6 11a2.8 2.8 0 0 0 2.3 1.2c1.7 0 3.1-1.4 3.1-3.4V8a8 8 0 0 0-8-8zm0 5.6a2.4 2.4 0 1 1 0 4.8 2.4 2.4 0 0 1 0-4.8z"/></svg>
          daniel@k7dynamics.com
        </li>
        <li>
          <svg viewBox="0 0 16 16" aria-hidden="true"><path d="M8 0a8 8 0 1 0 0 16A8 8 0 0 0 8 0zm5.9 7h-2.6a12 12 0 0 0-1-4.8A6 6 0 0 1 13.9 7zM8 2c.7 1 1.3 2.8 1.4 5H6.6C6.7 4.8 7.3 3 8 2zM5.7 2.2a12 12 0 0 0-1 4.8H2.1a6 6 0 0 1 3.6-4.8zM2.1 9h2.6a12 12 0 0 0 1 4.8A6 6 0 0 1 2.1 9zM8 14c-.7-1-1.3-2.8-1.4-5h2.8c-.1 2.2-.7 4-1.4 5zm2.3-.2a12 12 0 0 0 1-4.8h2.6a6 6 0 0 1-3.6 4.8z"/></svg>
          www.k7dynamics.com
        </li>
      </ul>
    </div>
  </section>

  <section class="card card-back" aria-label="Business card back">
    <div class="brand">
      <div class="brand-row">
        <span class="brand-dot"></span>
        <span class="brand-name">K7 Dynamics</span>
      </div>
      <span class="brand-tagline">Web Design, Development and Marketing</span>
    </div>
  </section>

</body>
</html>
```